Fairbrook's Vacation Rentals Business Card

Multi Million dollar villa rentals in the Dominican Republic.

Industry/Entity Type

Business

Contact Information for Business Card

I am looking for a high-end look around my company name/logo (see attached) on one side incorporating the following info: first and last name, title, address, phone #, email and company website. On the backside I want to add a full color picture of one of our villas (see attached).

```html
<!DOCTYPE html>
<html lang="en">
<head>
<meta charset="utf-8">
<title>Fairbrook's Vacation Rentals – Business Card</title>
<link href="https://fonts.googleapis.com/css2?family=Questrial&display=swap" rel="stylesheet">
<style>
  :root {
    --backdrop: #2b2b2d;
    --card: #ffffff;
    --orange: #f7941d;
    --ink: #231f20;
    --text: #3a3a3a;
    --sky: #6f9fd6;
    --villa: #e9ebe6;
    --pool: #1f6fc4;
  }
  * { margin: 0; padding: 0; box-sizing: border-box; }
  html, body { width: 1200px; height: 900px; overflow: hidden; }
  body {
    background: var(--backdrop);
    font-family: "Questrial", "Century Gothic", sans-serif;
    color: var(--text);
    position: relative;
  }
  .card {
    position: absolute;
    left: 250px;
    width: 700px;
    height: 400px;
    background: var(--card);
    overflow: hidden;
  }
  .card--photo { top: 35px; }
  .card--details { top: 465px; }

  .wordmark {
    display: flex;
    align-items: center;
    gap: 12px;
  }
  .wordmark__dot {
    width: 34px; height: 34px;
    border-radius: 50%;
    background: var(--orange);
    flex: none;
  }
  .wordmark__name {
    color: var(--ink);
    font-size: 27px;
    line-height: 1.05;
    letter-spacing: 0.5px;
  }

  .card--photo .wordmark {
    position: absolute;
    left: 200px; top: 28px;
  }
  .photo-divider {
    position: absolute;
    left: 0; right: 0; top: 106px;
    height: 5px;
    background: var(--orange);
  }
  .villa-photo {
    position: absolute;
    left: 0; right: 0; top: 111px; bottom: 0;
    background: linear-gradient(180deg, var(--sky) 0%, #a9c6e6 22%, var(--villa) 38%, #d8d6cc 70%, var(--pool) 82%, #2a86d8 100%);
  }

  .card--details .wordmark {
    position: absolute;
    left: 62px; top: 72px;
  }
  .frame-left {
    position: absolute;
    left: 40px; top: 50px;
    width: 5px; height: 240px;
    background: var(--orange);
  }
  .frame-bottom {
    position: absolute;
    left: 40px; top: 285px;
    width: 540px; height: 5px;
    background: var(--orange);
  }
  .person {
    position: absolute;
    right: 90px; top: 220px;
    text-align: right;
  }
  .person__name {
    color: var(--orange);
    font-size: 25px;
    line-height: 1.1;
    letter-spacing: 0.5px;
    text-transform: uppercase;
  }
  .person__title {
    display: block;
    font-size: 15px;
    line-height: 1.3;
    color: var(--ink);
  }
  .address {
    position: absolute;
    right: 40px; top: 302px;
    text-align: right;
    font-size: 15px;
    font-style: normal;
    line-height: 1.45;
    color: var(--ink);
  }
  .contacts {
    position: absolute;
    left: 58px; top: 308px;
    list-style: none;
    font-size: 15px;
    line-height: 1.6;
    color: var(--ink);
  }
  .contacts li { display: flex; align-items: center; gap: 10px; }
  .contacts svg { width: 13px; height: 13px; flex: none; }
  .contacts .accent { color: var(--orange); }
  .tick-mark {
    position: absolute;
    left: 170px; bottom: 0;
    width: 4px; height: 14px;
    background: var(--orange);
  }
</style>
</head>
<body>

  <section class="card card--photo">
    <div class="wordmark">
      <span class="wordmark__dot"></span>
      <span class="wordmark__name">Fairbrook's<br>Vacation Rentals</span>
    </div>
    <div class="photo-divider"></div>
    <div class="villa-photo" role="img" aria-label="Photograph of a white two-storey villa with terracotta roof, arched terrace, palm trees and a blue swimming pool with loungers"></div>
  </section>

  <section class="card card--details">
    <div class="frame-left"></div>
    <div class="frame-bottom"></div>

    <div class="wordmark">
      <span class="wordmark__dot"></span>
      <span class="wordmark__name">Fairbrook's<br>Vacation Rentals</span>
    </div>

    <div class="person">
      <div class="person__name">Maren Ellsworth</div>
      <span class="person__title">Founder</span>
    </div>

    <address class="address">
      Level 14 , Coral Bay Tower<br>
      Harbor View Street, Port Alma 40718
    </address>

    <ul class="contacts">
      <li>
        <svg viewBox="0 0 16 16" aria-hidden="true"><path fill="#f7941d" d="M3.6 1.2l2.3 2.8-1.2 1.6c.9 2 2.4 3.6 4.5 4.6l1.6-1.2 2.8 2.3-1.3 2.5C7.4 13.5 2.3 8.4 1.1 3.5z"/></svg>
        +1 809 555 0142
      </li>
      <li>
        <svg viewBox="0 0 16 16" aria-hidden="true"><rect x="1" y="3" width="14" height="10" fill="none" stroke="#f7941d" stroke-width="1.8"/><path d="M1 3l7 6 7-6" fill="none" stroke="#f7941d" stroke-width="1.8"/></svg>
        fairbrooks@fbrentals.com
      </li>
      <li>
        <svg viewBox="0 0 16 16" aria-hidden="true"><circle cx="8" cy="8" r="6.5" fill="none" stroke="#f7941d" stroke-width="1.6"/><path d="M1.5 8h13M8 1.5c-3 3.5-3 9.5 0 13M8 1.5c3 3.5 3 9.5 0 13" fill="none" stroke="#f7941d" stroke-width="1.3"/></svg>
        <span>www.<span class="accent">fbvacationrentals</span>.com</span>
      </li>
    </ul>
    <div class="tick-mark"></div>
  </section>

</body>
</html>
```